New Alcoholic Spiked Seltzer Line

We need a can design for a line of low calorie alcoholic seltzer. This product is a sparkling water and vodka drink with no sugar added in a slim 12 oz can.

This is a lighter, healthier, alternative to the sugary ready-to-drinks on the market. The product contains only 3 ingredients: Vodka, Water and Natural Flavors. It has only 100 calories but still has 5% alcohol, so you don't need to sacrifice alcohol to cut calories.

This product also does not contain any preservatives.

We want this design to communicate the following objectives to the consumer and in this order:

1. Appetizing product
2.Low calorie
3.Communicate the type of beverage (Spiked Seltzer)

The brand name of the product is VELKA.

The flavor of the product needed to be used for the design is Mango-Orange.

Comparable products are:

www.brisavelfizz.example/
https://www.tarnowbubble.example
https://quellrind.example/

The designs should not infringe or copy the creative directions of the products mentionned above. They are only given so that you can better understand the type of product we are developing.

Target Market(s)

Young Professional women between the ages of 25 and 44

Industry/Entity Type

Product

Colors

Designer to choose colors to be used in the design.

Requirements
Must have
• Design extendibility, meaning it can be adapted for other flavors.
• This is a new category in the market we are targeting, so consumers must easily be able to identify what type of product this is.

```html
<!DOCTYPE html>
<html lang="en">
<head>
<meta charset="UTF-8">
<title>VELKA Mango Orange Spiked Seltzer – Label</title>
<link href="https://fonts.googleapis.com/css2?family=Quicksand:wght@500;700&display=swap" rel="stylesheet">
<style>
  :root {
    --bg-light: #f2f4f5;
    --bg-shade: #dfe3e6;
    --sky: #4aa8e0;
    --sky-deep: #2f86c6;
    --mango: #f0a54a;
    --mango-deep: #e8943a;
    --label-white: #ffffff;
    --fruit-warm: #e98a3a;
    --fruit-red: #c9463a;
  }
  * { margin: 0; padding: 0; box-sizing: border-box; }
  html, body { width: 1200px; height: 989px; overflow: hidden; }
  body {
    background: radial-gradient(ellipse at center, var(--bg-light) 35%, var(--bg-shade) 100%);
    font-family: "Quicksand", sans-serif;
    position: relative;
  }
  .can-label {
    position: absolute;
    left: 380px;
    top: 105px;
    width: 440px;
    height: 780px;
    background: var(--label-white);
    overflow: hidden;
    border-radius: 6px;
    box-shadow: 0 6px 24px rgba(0,0,0,0.08);
  }
  .label-shapes { position: absolute; inset: 0; }
  .brand-name {
    position: absolute;
    left: 0; right: 0;
    top: 120px;
    text-align: center;
    font-weight: 700;
    font-size: 104px;
    letter-spacing: 2px;
    color: var(--label-white);
    line-height: 1;
  }
  .calorie-badge {
    position: absolute;
    left: 22px; top: 270px;
    width: 120px; height: 120px;
    border-radius: 50%;
    background: var(--sky);
    color: var(--label-white);
    display: flex; flex-direction: column;
    align-items: center; justify-content: center;
    line-height: 1.05;
    font-weight: 500;
  }
  .calorie-badge .small { font-size: 19px; }
  .calorie-badge .number { font-size: 34px; font-weight: 700; }
  .flavor-name {
    position: absolute;
    left: 285px; top: 355px;
    transform: translate(-50%, -50%) rotate(-28deg);
    color: var(--mango);
    font-weight: 700;
    font-size: 46px;
    line-height: 0.95;
    letter-spacing: 1px;
    text-align: center;
    white-space: nowrap;
  }
  .product-type {
    position: absolute;
    left: 370px; top: 580px;
    transform: translate(-50%, -50%) rotate(-62deg);
    color: var(--label-white);
    font-weight: 500;
    font-size: 28px;
    white-space: nowrap;
  }
  .fruit-visual {
    position: absolute;
    left: 30px; top: 440px;
    width: 205px; height: 190px;
    border-radius: 50% 45% 40% 50%;
    background: radial-gradient(circle at 35% 45%, var(--mango) 0%, var(--fruit-warm) 45%, var(--fruit-red) 80%, rgba(201,70,58,0) 100%);
  }
  .abv {
    position: absolute;
    left: 40px; top: 688px;
    color: var(--mango-deep);
    font-weight: 700;
    font-size: 26px;
  }
</style>
</head>
<body>
  <main class="can-label">
    <svg class="label-shapes" width="440" height="780" viewBox="0 0 440 780" aria-hidden="true">
      <path d="M0,0 H440 V215 C330,250 110,250 0,225 Z" fill="var(--sky)"/>
      <path d="M0,0 H440 V70 C300,110 140,40 0,90 Z" fill="var(--sky-deep)" opacity="0.55"/>
      <path d="M440,380 C330,450 260,600 270,780 H440 Z" fill="var(--mango)"/>
      <g fill="var(--sky)">
        <circle cx="160" cy="262" r="7"/>
        <circle cx="182" cy="256" r="5"/>
        <circle cx="178" cy="280" r="10"/>
        <circle cx="160" cy="300" r="6"/>
      </g>
    </svg>

    <div class="brand-name">VELKA</div>

    <div class="calorie-badge">
      <span class="small">only</span>
      <span class="number">100</span>
      <span class="small">calories</span>
    </div>

    <div class="flavor-name">MANGO<br>ORANGE</div>

    <div class="product-type">Spiked Seltzer</div>

    <div class="fruit-visual" role="img" aria-label="Photo of a ripe mango, orange halves and ice cubes"></div>

    <div class="abv">5% alc./ vol.</div>
  </main>
</body>
</html>
```